Cedar Bend (by the numbers)

We (city communications office of Cedar Bend, Arkansas) are launching a magazine to be delivered to every house in the community. We would like the first inside page to be an infographic of the important and interesting "numbers" from 2017. We want it to be visually interesting and convey the huge amount of important services we provide our residents. I have included a document with the relevant statistics to be used.

Target Market(s)

Residents of our city

Industry/Entity Type

House

Colors

Designer to choose colors to be used in the design.

Requirements
Must have
• Our logo must be prominent. The dimensions should be able to fit onto a standard full page magazine. If the infographic is best displayed on two pages we will accept that as well, and change our layout.
Nice to have
• Not every statistic we have provided must be used but if they can be, that is preferable. I have also included some inspirational infographics that appealed to me and inspired the idea, but I am excited about new concepts that might not look anything like those that I have provided.
Should not have
• The design should not have anything incorporated that cannot be presented to families in our community. It must be all ages friendly.

```html
<!DOCTYPE html>
<html lang="en">
<head>
<meta charset="utf-8">
<title>Cedar Bend by the Numbers 2017</title>
<link href="https://fonts.googleapis.com/css2?family=Roboto+Condensed:wght@400;500;700&family=Roboto:wght@400;500&display=swap" rel="stylesheet">
<style>
  :root {
    --paper: #eeeeef;
    --band: #d3d3d5;
    --navy: #1f3a8f;
    --navy-deep: #17307a;
    --orange: #f57c1f;
    --red: #e8242a;
    --yellow: #fcd21c;
    --ink: #1c1c1c;
    --truck: #3c9a3f;
    --cab: #b9bcbf;
    --road: #3a3a3a;
    --footer: #3b3b3b;
    --white: #ffffff;
  }
  * { margin: 0; padding: 0; box-sizing: border-box; }
  html, body { width: 924px; height: 1200px; overflow: hidden; background: var(--paper); }
  .infographic {
    position: relative; width: 924px; height: 1200px;
    background: var(--paper);
    font-family: "Roboto Condensed", "Arial Narrow", sans-serif;
  }
  .abs { position: absolute; }

  .title-box {
    left: 0; top: 0; width: 722px; height: 124px;
    background: var(--yellow);
    padding: 26px 0 0 20px;
    color: var(--red); font-weight: 700; font-size: 31px; line-height: 42px;
  }
  .year {
    left: 440px; top: 0;
    font-family: "Roboto", sans-serif; font-weight: 500;
    font-size: 116px; line-height: 124px; color: var(--navy);
  }
  .brand {
    left: 732px; top: 0; width: 192px; height: 199px;
    background: var(--white);
    display: flex; align-items: center; justify-content: center; flex-direction: column; gap: 10px;
    color: var(--navy); font-weight: 700; font-size: 30px; text-align: center; line-height: 32px;
  }
  .brand-mark { width: 26px; height: 26px; border-radius: 50%; background: var(--navy); }

  .people {
    left: 28px; top: 237px; width: 527px; height: 207px;
    display: grid; grid-template-columns: repeat(11, 1fr); grid-template-rows: 1fr 1fr;
    column-gap: 16px; row-gap: 16px;
  }
  .people .unit { background: linear-gradient(180deg, #f9a25f, var(--orange)); border-radius: 16px 16px 4px 4px; }
  .pop-label { left: 590px; top: 250px; font-size: 66px; line-height: 80px; font-weight: 700; color: var(--orange); }
  .pop-value {
    left: 580px; top: 330px;
    font-family: "Roboto", sans-serif; font-size: 106px; line-height: 120px; font-weight: 500; color: var(--navy);
  }

  .calls-band { left: 0; top: 464px; width: 924px; height: 356px; background: var(--band); }
  .portrait { border-radius: 50%; background: radial-gradient(circle at 50% 40%, #2c4fb0, var(--navy-deep)); }
  .portrait.fire { left: 116px; top: 495px; width: 190px; height: 190px; }
  .portrait.police { left: 617px; top: 475px; width: 184px; height: 184px; }
  .phone { width: 82px; height: 82px; }
  .phone.fire { left: 114px; top: 670px; }
  .phone.police { left: 718px; top: 670px; transform: scaleX(-1); }
  .stat-number {
    font-family: "Roboto", sans-serif; font-weight: 500; font-size: 74px; line-height: 74px; color: var(--navy);
  }
  .stat-caption { font-size: 28px; line-height: 34px; color: var(--ink); font-weight: 500; }
  .fire-calls { left: 198px; top: 686px; }
  .police-calls { left: 512px; top: 686px; }

  .garbage-title { left: 20px; top: 846px; font-size: 59px; line-height: 70px; color: var(--ink); font-weight: 500; }
  .garbage-value {
    left: 62px; top: 982px;
    font-family: "Roboto", sans-serif; font-weight: 500; font-size: 100px; line-height: 110px; color: var(--navy);
  }
  .truck {
    left: 460px; top: 935px; width: 413px; height: 160px;
    background: linear-gradient(90deg, var(--cab), #8fb58f 30%, var(--truck) 55%, #2f7f33);
    border-radius: 14px 14px 6px 6px;
  }
  .road { left: 46px; top: 1096px; width: 827px; height: 10px; background: var(--road); border-radius: 5px; }

  .footer {
    left: 0; top: 1146px; width: 924px; height: 54px; background: var(--footer);
    color: var(--white); font-family: "Roboto", sans-serif; font-size: 22px;
    display: flex; align-items: center; justify-content: center;
  }
</style>
</head>
<body>
<main class="infographic">
  <div class="abs title-box">Cedar Bend (CB)<br>by the Numbers (#'s)</div>
  <div class="abs year">2017</div>
  <div class="abs brand"><span class="brand-mark"></span>CEDAR<br>BEND</div>

  <div class="abs people" role="img" aria-label="Unit chart of residents in two rows of eleven">
    <span class="unit"></span><span class="unit"></span><span class="unit"></span><span class="unit"></span><span class="unit"></span><span class="unit"></span><span class="unit"></span><span class="unit"></span><span class="unit"></span><span class="unit"></span><span class="unit"></span>
    <span class="unit"></span><span class="unit"></span><span class="unit"></span><span class="unit"></span><span class="unit"></span><span class="unit"></span><span class="unit"></span><span class="unit"></span><span class="unit"></span><span class="unit"></span><span class="unit"></span>
  </div>
  <div class="abs pop-label">Population</div>
  <div class="abs pop-value">65,004</div>

  <section class="abs calls-band"></section>
  <div class="abs portrait fire" role="img" aria-label="Firefighter illustration in a blue circle"></div>
  <div class="abs portrait police" role="img" aria-label="Police officer illustration in a blue circle"></div>
  <svg class="abs phone fire" viewBox="0 0 24 24" aria-hidden="true">
    <path fill="#1c1c1c" d="M6.6 10.8a15.1 15.1 0 0 0 6.6 6.6l2.2-2.2a1 1 0 0 1 1-.25 11.4 11.4 0 0 0 3.6.57 1 1 0 0 1 1 1V20a1 1 0 0 1-1 1A17 17 0 0 1 3 4a1 1 0 0 1 1-1h3.5a1 1 0 0 1 1 1c0 1.25.2 2.45.57 3.57a1 1 0 0 1-.25 1z"/>
  </svg>
  <svg class="abs phone police" viewBox="0 0 24 24" aria-hidden="true">
    <path fill="#1c1c1c" d="M6.6 10.8a15.1 15.1 0 0 0 6.6 6.6l2.2-2.2a1 1 0 0 1 1-.25 11.4 11.4 0 0 0 3.6.57 1 1 0 0 1 1 1V20a1 1 0 0 1-1 1A17 17 0 0 1 3 4a1 1 0 0 1 1-1h3.5a1 1 0 0 1 1 1c0 1.25.2 2.45.57 3.57a1 1 0 0 1-.25 1z"/>
  </svg>
  <div class="abs fire-calls">
    <div class="stat-number">12,560</div>
    <div class="stat-caption">Fire 911 calls</div>
  </div>
  <div class="abs police-calls">
    <div class="stat-number">26,660</div>
    <div class="stat-caption">Police 911 calls</div>
  </div>

  <div class="abs garbage-title">Tons of Household garbage collected</div>
  <div class="abs garbage-value">16,768</div>
  <div class="abs truck" role="img" aria-label="Green garbage truck beside a roadside bin"></div>
  <div class="abs road"></div>

  <footer class="abs footer">www.cedarbend.gov/</footer>
</main>
</body>
</html>
```